Hospice pharmacy billing program needing a brochure

We are looking for an informative brochure that will convey the potential savings a hospice agency will experience by using us as their PBM (pharmacy benefit manager). We pay their pharmacies for all medications administered to their patients, and by our ability to broker cheaper rates with pharmacies we are able to reduce the drug cost to the hospice agency.

I've included our company logo, it would be preferable to utilize the tones of green and blue for any backgrounds or graphic images on the product.

We want to convey that we are a national program, we will reduce their (hospice agencies) drug costs, and we can provide them with their CMS 8358 reports. These reports consist of many fields of information required by Medicare in a specific format that will import into their software.

We would also like our contact information on the brochure:
Phone: 855-347-6182
Email: Support@CarewellRx.com
Website: CarewellRx.com

Please email me with any questions at Dmorrow@CarewellRx.com

Thank you for your time,
Derek Morrow

```html
<!DOCTYPE html>
<html lang="en">
<head>
<meta charset="utf-8">
<title>CarewellRx Brochure</title>
<link href="https://fonts.googleapis.com/css2?family=Arimo:wght@400;700&family=Noto+Serif:ital@1&display=swap" rel="stylesheet">
<style>
  :root {
    --navy: #0e5580;
    --sage: #9db06a;
    --paper: #faf6f2;
    --white: #ffffff;
    --ink: #2b2320;
    --scrub-light: #e6f2f8;
    --scrub: #8fcbe6;
    --scrub-deep: #6fb6d8;
    --backdrop: #ece6dc;
  }
  * { margin: 0; padding: 0; box-sizing: border-box; }
  html, body { width: 1200px; height: 1200px; overflow: hidden; }
  body { background: var(--backdrop); font-family: "Arimo", Arial, sans-serif; color: var(--ink); position: relative; }

  .spread { position: absolute; width: 660px; height: 511px; background: var(--paper); overflow: hidden; box-shadow: 0 3px 8px rgba(0,0,0,.25); }
  .spread-outer { left: 36px; top: 64px; }
  .spread-inner { left: 486px; top: 654px; }
  .spread svg.graphics { position: absolute; inset: 0; }

  /* outer spread */
  .brand { position: absolute; left: 70px; top: 201px; display: flex; align-items: center; gap: 8px; }
  .brand-square { width: 28px; height: 28px; background: var(--navy); }
  .brand-name { font-size: 25px; font-weight: 400; color: var(--navy); }

  .tagline { position: absolute; left: 337px; top: 12px; font-family: "Noto Serif", Georgia, serif; font-style: italic; font-size: 14.5px; line-height: 24px; color: var(--navy); }
  .tagline span { display: block; }
  .tagline span + span { padding-left: 30px; }

  .contact { position: absolute; left: 514px; top: 470px; font-size: 8px; font-weight: 700; line-height: 10px; color: var(--white); font-style: normal; }

  /* inner spread */
  .panel { position: absolute; top: 0; width: 310px; }
  .panel-left { left: 16px; }
  .panel-right { left: 341px; }
  .heading { position: absolute; font-size: 11px; font-weight: 700; color: #2f2622; white-space: nowrap; }
  .copy { position: absolute; font-size: 8.3px; line-height: 11px; }
  .marked { padding-left: 16px; }
  .marked::before { content: "\2723"; position: absolute; left: 0; font-size: 10px; color: var(--ink); }
  .list { position: absolute; list-style: none; font-size: 8.3px; line-height: 15px; }
  .list li { position: relative; padding-left: 12px; white-space: nowrap; }
  .list li::before { content: "\2723"; position: absolute; left: 0; font-size: 8px; color: #5d524c; }
  .list li .cont { display: block; padding-left: 3px; }
</style>
</head>
<body>

<section class="spread spread-outer" aria-label="Brochure outside: back and front cover">
  <svg class="graphics" viewBox="0 0 660 511" width="660" height="511">
    <defs>
      <clipPath id="front-white-area">
        <path d="M330,0 L531,0 C580,30 605,95 600,160 C595,300 470,415 330,478 Z"/>
      </clipPath>
      <linearGradient id="scrubs-tone" x1="0" y1="0" x2="0" y2="1">
        <stop offset="0" stop-color="var(--scrub-light)"/>
        <stop offset="0.5" stop-color="var(--scrub)"/>
        <stop offset="1" stop-color="var(--scrub-deep)"/>
      </linearGradient>
    </defs>
    <g aria-hidden="true">
      <rect x="330" y="0" width="330" height="511" fill="var(--navy)"/>
      <path d="M330,0 L541,0 C592,32 612,100 608,162 C602,305 480,425 330,486 Z" fill="var(--sage)"/>
      <path d="M330,0 L531,0 C580,30 605,95 600,160 C595,300 470,415 330,478 Z" fill="var(--white)"/>
      <rect x="0" y="472" width="334" height="14" fill="var(--sage)"/>
      <rect x="0" y="486" width="660" height="25" fill="var(--navy)"/>
    </g>
    <g role="img" aria-label="Photo of a smiling nurse in light blue scrubs holding a clipboard" clip-path="url(#front-white-area)">
      <path d="M343,443 L343,200 C343,120 400,73 460,73 C520,73 577,120 577,200 L577,443 Z" fill="url(#scrubs-tone)"/>
    </g>
  </svg>

  <div class="brand">
    <span class="brand-square"></span>
    <span class="brand-name">CarewellRx</span>
  </div>

  <p class="tagline"><span>Save money by offering</span><span>lower-cost medication options.</span></p>

  <address class="contact">
    Phone: 855-347-6182<br>
    Email: Support@CarewellRx.com<br>
    Website: CarewellRx.com
  </address>
</section>

<section class="spread spread-inner" aria-label="Brochure inside: left and right panels">
  <svg class="graphics" viewBox="0 0 660 511" width="660" height="511" aria-hidden="true">
    <path d="M588,0 L660,0 L660,511 L331,511 L331,486 C460,470 560,440 630,370 C700,300 690,80 588,0 Z" fill="var(--sage)"/>
    <path d="M598,0 L660,0 L660,511 L331,511 L331,486 C465,476 570,446 640,376 C706,300 695,80 598,0 Z" fill="var(--navy)"/>
    <rect x="0" y="479" width="340" height="7" fill="var(--sage)"/>
    <rect x="0" y="486" width="660" height="25" fill="var(--navy)"/>
  </svg>

  <div class="panel panel-left">
    <h2 class="heading" style="top:21px">Reduced drug costs for hospice agencies nationwide</h2>
    <p class="copy marked" style="top:57px;width:297px">CarewellRx is a national pharmacy benefit manager built for hospice agencies. We pay your pharmacies for every medication administered to your patients, and because we broker lower rates with pharmacies across the country, your agency pays less for the same drugs. Administrators and nurses keep their current pharmacies while CarewellRx handles billing, payment and pricing. Wherever your patients are, we are there.</p>
    <p class="copy marked" style="top:156px;width:297px">Patients are your priority. Their comfort and well-being are in your hands. When your staff spends valuable time sorting pharmacy invoices, checking prices, or preparing Medicare paperwork, it takes time away from those who need you most. CarewellRx understands the unique challenges faced by the hospice industry because it's the only industry we serve. Our mission is to help you improve patient care and business operations.</p>
    <h2 class="heading" style="top:263px">Services that make a difference</h2>
    <p class="copy" style="top:301px;left:16px;width:285px">Choosing CarewellRx as your PBM will have an immediate impact on your patients, your staff, and your business. We'll help you:</p>
    <ul class="list" style="top:337px;left:14px;width:290px">
      <li>Save money with pharmacy rates we negotiate on your behalf.</li>
      <li>Save time with one consolidated bill for all of your <span class="cont">patients' medications.</span></li>
      <li>Meet Medicare requirements with complete CMS 8358 reports <span class="cont">formatted to import into your software.</span></li>
      <li>Serve patients anywhere through our national network of <span class="cont">participating pharmacies.</span></li>
      <li>Increase efficiency with a single point of contact.</li>
    </ul>
  </div>

  <div class="panel panel-right">
    <h2 class="heading" style="top:21px">Why Hospice Agencies Choose CarewellRx</h2>
    <ul class="list" style="top:57px;left:8px;width:300px">
      <li>Focused exclusively on hospice care</li>
      <li>National program serving hospice agencies in every state</li>
      <li>Lower negotiated drug rates that reduce your medication costs</li>
      <li>We pay your pharmacies for all administered medications</li>
      <li>CMS 8358 reports in the exact format your software imports</li>
      <li>Eliminates costly administrative work for staff, such as invoice <span class="cont">review</span></li>
    </ul>
    <h2 class="heading" style="top:195px">Values that make a difference</h2>
    <p class="copy" style="top:229px;left:8px;width:300px">Our patient-focused values make a difference in every exchange we have with pharmacies, nurses, and hospice administrators. When you choose CarewellRx, you'll get a trusted partner committed to helping you improve patient care, reduce overall pharmaceutical costs, and optimize profits. We value:</p>
    <ul class="list" style="top:294px;left:8px;width:300px">
      <li>Patient quality of life.</li>
      <li>Respectful, responsive communication with everyone we serve.</li>
      <li>Honest, sincere answers to difficult questions.</li>
      <li>Transparency in all our dealings.</li>
      <li>Innovation that leads to better business practices.</li>
    </ul>
  </div>
</section>

</body>
</html>
```